Great Opportunity !! Masters in Business Analytics College Course

the size is Full Page, with bleed*
8”x 10.75" plus 0.25" bleed.
please leave one inch for footer
the purpose is attract students to join this college program .
this is for students in USA .
college age of around 24 years old
I am looking for a flyer that is unique and shows creativity .
A flyer that people would want to look at it because it is unique.
you can choose either vector, text ,or picture.
if you do picture it should be a white USA citizen wearing a white solid shirt and not long hair

Target Market(s)

USA students about 23 in age to join this college program

Industry/Entity Type

education

Colors
0054AA
0677BA
7BADD7
CADEEF
E8F1F8
0094D4
00A9DD
6FCCEA
C7EBF8
E9F6FB

Requirements
Must have
• the text should not be crowded .. .. .. the ad should not be full of text
Should not have
• not have very large text .. it should not be a flyer that is full of text .. you have to figure out how to avoid looking at the ad and it is very busy with text

```html
<!DOCTYPE html>
<html lang="en">
<head>
<meta charset="utf-8">
<title>Master's in Business Analytics – Harlow State College</title>
<link href="https://fonts.googleapis.com/css2?family=Bebas+Neue&family=Montserrat:ital,wght@0,400;0,500;0,600;0,700;1,800&display=swap" rel="stylesheet">
<style>
  :root {
    --navy: #0054AA;
    --blue: #0677BA;
    --sky: #6FCCEA;
    --ice: #C7EBF8;
    --mist: #E9F6FB;
    --pale: #CADEEF;
    --white: #ffffff;
    --ink: #0b2545;
    --footer-text: #e6e6e6;
  }
  html, body {
    margin: 0;
    padding: 0;
    width: 920px;
    height: 1200px;
    overflow: hidden;
    background: var(--white);
  }
  .flyer {
    position: relative;
    width: 920px;
    height: 1200px;
    font-family: "Montserrat", Arial, sans-serif;
    color: var(--white);
  }
  .panel {
    position: absolute;
    left: 0; top: 0;
    width: 920px; height: 1097px;
    background: var(--navy);
    overflow: hidden;
  }
  .headline {
    position: absolute;
    left: 39px; top: 26px;
    margin: 0;
    font-weight: 500;
    font-size: 37px;
    line-height: 53px;
    letter-spacing: 0.2px;
  }
  .program-band {
    position: absolute;
    left: 0; top: 143px;
    width: 720px; height: 88px;
  }
  .program-title {
    position: absolute;
    left: 43px; top: 152px;
    margin: 0;
    color: var(--ink);
    font-weight: 600;
    font-size: 28px;
    line-height: 35px;
  }
  .condensed {
    position: absolute;
    left: 43px;
    margin: 0;
    font-family: "Bebas Neue", Impact, sans-serif;
    font-weight: 400;
    line-height: 1;
  }
  .lead-in { top: 288px; font-size: 31px; }
  .salary-line { top: 317px; font-size: 94px; }
  .salary-figure { top: 402px; font-size: 94px; color: var(--sky); }
  .source { top: 488px; font-size: 43px; }
  .checklist {
    position: absolute;
    left: 45px;
    margin: 0; padding: 0;
    list-style: none;
    font-size: 17.5px;
    line-height: 22px;
  }
  .checklist li {
    display: flex;
    align-items: center;
    gap: 8px;
  }
  .checklist svg { width: 15px; height: 15px; flex: none; }
  .roles { top: 552px; }
  .employers { top: 707px; }
  .hired-label {
    position: absolute;
    left: 43px; top: 652px;
    margin: 0;
    font-weight: 600;
    font-size: 19px;
    line-height: 21px;
  }
  .event-title { top: 855px; font-size: 42px; color: var(--sky); }
  .event-date {
    position: absolute;
    left: 43px; top: 891px;
    margin: 0;
    font-weight: 700;
    font-size: 20.5px;
  }
  .event-contact {
    position: absolute;
    left: 43px; top: 918px;
    margin: 0;
    font-size: 15.5px;
  }
  .college-name { top: 960px; font-size: 42px; color: var(--sky); }
  .accreditation {
    position: absolute;
    left: 43px; top: 998px;
    margin: 0;
    font-size: 16.5px;
    line-height: 21px;
  }
  .format {
    position: absolute;
    left: 43px; top: 1059px;
    margin: 0;
    font-size: 13px;
  }
  .format strong { font-weight: 800; font-style: italic; }
  .photo {
    position: absolute;
    left: 590px; top: 420px;
    width: 330px; height: 677px;
  }
  .footer {
    position: absolute;
    left: 0; top: 1097px;
    width: 920px; height: 103px;
    display: flex;
    align-items: center;
    justify-content: center;
    font-weight: 600;
    font-size: 30px;
    letter-spacing: 25px;
    color: var(--footer-text);
  }
</style>
</head>
<body>
<div class="flyer">
  <section class="panel">
    <svg class="photo" viewBox="0 0 330 677" role="img" aria-label="Photo of a smiling young man in a white shirt holding a blue folder, gesturing toward the text">
      <defs>
        <linearGradient id="photo-fill" x1="0" y1="0" x2="0" y2="1">
          <stop offset="0" stop-color="var(--blue)"/>
          <stop offset="1" stop-color="var(--pale)"/>
        </linearGradient>
      </defs>
      <rect width="330" height="677" fill="url(#photo-fill)"/>
    </svg>

    <h1 class="headline">Do You Have An Analytical Mind And<br>Seeking A Profitable Career?</h1>

    <svg class="program-band" viewBox="0 0 720 88" aria-hidden="true">
      <polygon points="0,0 681,0 720,88 0,88" fill="var(--ice)"/>
    </svg>
    <p class="program-title">A MASTER'S IN BUSINESS<br>ANALYTICS HARLOW STATE COLLEGE</p>

    <p class="condensed lead-in">Can prepare you for some of the most in-demand jobs.</p>
    <p class="condensed salary-line">Jobs with a median</p>
    <p class="condensed salary-figure">Salary of $100K+</p>
    <p class="condensed source">(US Bureau of Labor Statistics 2023)</p>

    <ul class="checklist roles">
      <li><svg viewBox="0 0 16 16"><rect x="1" y="3" width="12" height="12" rx="2" fill="none" stroke="var(--sky)" stroke-width="2"/><path d="M4 8.5l3 3 8-9" fill="none" stroke="var(--sky)" stroke-width="2.2"/></svg>BI Developer</li>
      <li><svg viewBox="0 0 16 16"><rect x="1" y="3" width="12" height="12" rx="2" fill="none" stroke="var(--sky)" stroke-width="2"/><path d="M4 8.5l3 3 8-9" fill="none" stroke="var(--sky)" stroke-width="2.2"/></svg>Data Analyst</li>
      <li><svg viewBox="0 0 16 16"><rect x="1" y="3" width="12" height="12" rx="2" fill="none" stroke="var(--sky)" stroke-width="2"/><path d="M4 8.5l3 3 8-9" fill="none" stroke="var(--sky)" stroke-width="2.2"/></svg>Data Scientist</li>
      <li><svg viewBox="0 0 16 16"><rect x="1" y="3" width="12" height="12" rx="2" fill="none" stroke="var(--sky)" stroke-width="2"/><path d="M4 8.5l3 3 8-9" fill="none" stroke="var(--sky)" stroke-width="2.2"/></svg>Data Developer</li>
    </ul>

    <p class="hired-label">Graduates<br>were hired at:</p>

    <ul class="checklist employers">
      <li><svg viewBox="0 0 16 16"><rect x="1" y="3" width="12" height="12" rx="2" fill="none" stroke="var(--sky)" stroke-width="2"/><path d="M4 8.5l3 3 8-9" fill="none" stroke="var(--sky)" stroke-width="2.2"/></svg>Vantrex Pharma</li>
      <li><svg viewBox="0 0 16 16"><rect x="1" y="3" width="12" height="12" rx="2" fill="none" stroke="var(--sky)" stroke-width="2"/><path d="M4 8.5l3 3 8-9" fill="none" stroke="var(--sky)" stroke-width="2.2"/></svg>Calder &amp; Reyes</li>
      <li><svg viewBox="0 0 16 16"><rect x="1" y="3" width="12" height="12" rx="2" fill="none" stroke="var(--sky)" stroke-width="2"/><path d="M4 8.5l3 3 8-9" fill="none" stroke="var(--sky)" stroke-width="2.2"/></svg>Nordline Systems</li>
      <li><svg viewBox="0 0 16 16"><rect x="1" y="3" width="12" height="12" rx="2" fill="none" stroke="var(--sky)" stroke-width="2"/><path d="M4 8.5l3 3 8-9" fill="none" stroke="var(--sky)" stroke-width="2.2"/></svg>Voltair Motors</li>
      <li><svg viewBox="0 0 16 16"><rect x="1" y="3" width="12" height="12" rx="2" fill="none" stroke="var(--sky)" stroke-width="2"/><path d="M4 8.5l3 3 8-9" fill="none" stroke="var(--sky)" stroke-width="2.2"/></svg>Keystead Insurance</li>
    </ul>

    <p class="condensed event-title">Open House</p>
    <p class="event-date">Wednesday, April 20, 7:30 pm.</p>
    <p class="event-contact">Email admissions@harlowstate.edu&nbsp; for the link!</p>

    <p class="condensed college-name">Harlow State College</p>
    <p class="accreditation">Only 5% of universities achieve prestigious<br>NABE accreditation."</p>

    <p class="format"><strong>21 MONTHS</strong> Hybrid with one weekly in-person evening meeting</p>
  </section>

  <footer class="footer">1 INCH FOOTER</footer>
</div>
</body>
</html>
```